1923 Basins & Spouts Business Card

I'm wanting to get a business card designed. Our business is 1923 Basins & Spouts
Details for the card:

1923 Basins & Spouts
Name: Gareth Vostle
Email: gareth@1923basinsandspouts.com.au
Website: www.1923basinsandspouts.com.au
Mobile: 0439 602 158
Phone: 02 5550 1843

Font of Basins & Spouts is called Snell Roundhand. Not sue what font logo text is.

I'm thinking two sided but it doesn't have to be.

```html
<!DOCTYPE html>
<html lang="en">
<head>
<meta charset="utf-8">
<title>1923 Basins &amp; Spouts — Business Card</title>
<link rel="stylesheet" href="https://fonts.googleapis.com/css2?family=Kaushan+Script&family=Lato:wght@400;700&display=swap">
<style>
  :root {
    --backdrop: #2a2a2a;
    --card: #ffffff;
    --ink: #111111;
    --ink-soft: #333333;
    --ornament: #d4d4d4;
    --ornament-fade: rgba(212,212,212,0);
  }
  * { box-sizing: border-box; margin: 0; padding: 0; }
  html, body {
    width: 1200px; height: 900px; overflow: hidden;
    background: var(--backdrop);
  }
  .stage {
    width: 1200px; height: 900px;
    display: flex; align-items: center; justify-content: center;
  }
  .card {
    position: relative;
    width: 1000px; height: 570px;
    background: var(--card);
    border-radius: 26px;
    overflow: hidden;
    font-family: "Lato", sans-serif;
    color: var(--ink);
  }
  .ornament-large {
    position: absolute; left: -40px; top: 120px;
    width: 520px; height: 480px;
    background: radial-gradient(ellipse at 40% 55%, var(--ornament) 0%, rgba(212,212,212,0.55) 40%, var(--ornament-fade) 70%);
  }
  .ornament-small {
    position: absolute; right: -50px; top: 150px;
    width: 200px; height: 300px;
    background: radial-gradient(ellipse at 65% 50%, rgba(212,212,212,0.8) 0%, rgba(212,212,212,0.4) 40%, var(--ornament-fade) 70%);
  }
  .brand {
    position: absolute; left: 0; right: 0; top: 70px;
    display: flex; align-items: center; justify-content: center; gap: 18px;
  }
  .brand-mark {
    width: 70px; height: 70px; border-radius: 50%;
    border: 2px solid var(--ink);
  }
  .brand-text { display: flex; flex-direction: column; gap: 6px; }
  .brand-name { font-size: 30px; font-weight: 400; color: var(--ink); }
  .brand-tagline { font-size: 12px; color: var(--ink-soft); letter-spacing: 0.2px; }
  .holder {
    position: absolute; left: 420px; top: 225px;
    font-family: "Kaushan Script", cursive;
    font-size: 44px; font-weight: 400; color: var(--ink);
  }
  .contacts {
    position: absolute; left: 520px; top: 305px;
    list-style: none;
    display: flex; flex-direction: column; gap: 14px;
  }
  .contact { display: flex; align-items: center; gap: 14px; font-size: 21px; color: var(--ink-soft); }
  .contact-icon { width: 32px; height: 32px; flex: none; }
  .website {
    position: absolute; left: 520px; top: 466px;
    font-size: 25px; font-weight: 700; color: var(--ink);
  }
</style>
</head>
<body>
<main class="stage">
  <article class="card">
    <div class="ornament-large" role="img" aria-label="Large grey floral swirl with leaves"></div>
    <div class="ornament-small" role="img" aria-label="Small grey floral swirl with leaves"></div>

    <header class="brand">
      <span class="brand-mark"></span>
      <div class="brand-text">
        <span class="brand-name">1923 Basins &amp; Spouts</span>
        <span class="brand-tagline">Pairing classic elegance with everyday function</span>
      </div>
    </header>

    <h1 class="holder">Gareth Vostle</h1>

    <ul class="contacts">
      <li class="contact">
        <svg class="contact-icon" viewBox="0 0 32 32" aria-hidden="true">
          <circle cx="16" cy="16" r="16" fill="#111"/>
          <rect x="11" y="7" width="10" height="18" rx="2" fill="none" stroke="#fff" stroke-width="1.8"/>
          <circle cx="16" cy="22" r="1" fill="#fff"/>
        </svg>
        <span>0439 602 158</span>
      </li>
      <li class="contact">
        <svg class="contact-icon" viewBox="0 0 32 32" aria-hidden="true">
          <circle cx="16" cy="16" r="16" fill="#111"/>
          <path d="M9 14 Q16 8 23 14 L21 16 L18 14 L14 14 L11 16 Z" fill="#fff"/>
          <rect x="10" y="17" width="12" height="7" rx="1.5" fill="#fff"/>
        </svg>
        <span>02 5550 1843</span>
      </li>
      <li class="contact">
        <svg class="contact-icon" viewBox="0 0 32 32" aria-hidden="true">
          <circle cx="16" cy="16" r="16" fill="#111"/>
          <rect x="8" y="10" width="16" height="12" fill="none" stroke="#fff" stroke-width="1.6"/>
          <path d="M8 10 L16 17 L24 10" fill="none" stroke="#fff" stroke-width="1.6"/>
        </svg>
        <span>gareth@1923basinsandspouts.com.au</span>
      </li>
    </ul>

    <p class="website">www.1923basinsandspouts.com.au</p>
  </article>
</main>
</body>
</html>
```